Startup Eyewear Store need Website

We are launching a new eyewear store. It's fun retro colors with bold wood tones. I will upload our logo to give you an idea of some fun colors. The site will need a cart and the ability to show multiple view of different eyewear frames. It will need standard buttons such as Contact Us, About Us, Blog, Social Media Feed, and New Releases, . The company will also have a Membership function and we need to be able to show that we can ship multiple frames have customers try them on and select which ones they want. We will need it responsive and all coding done.

Industry/Entity Type

Eyewear

Coding

Coded - Design and coding required

Number of Pages Required

1 page

Colors
f78f20

Requirements
Must have
• Clean Fund and Vintage Retro with some bright oranges.

```html
<!DOCTYPE html>
<html lang="en">
<head>
<meta charset="utf-8">
<title>Specs Parlour — Eyewear Store</title>
<link href="https://fonts.googleapis.com/css2?family=Lobster&family=Source+Sans+3:wght@400;600&display=swap" rel="stylesheet">
<style>
:root{
  --orange:#f18d22;
  --orange-soft:#f3a24f;
  --orange-deep:#e07a12;
  --cream:#f6f6f4;
  --white:#ffffff;
  --ink:#333333;
  --muted:#777777;
  --brown:#2a1a0d;
  --taupe:#b29c8e;
  --field:#f7efd4;
}
*{box-sizing:border-box;margin:0;padding:0}
html,body{width:1200px;height:2290px;overflow:hidden}
body{background:var(--cream);font-family:"Source Sans 3",Arial,sans-serif;color:var(--ink);position:relative}
.script{font-family:"Lobster",cursive;font-weight:400}
section,header,footer{position:absolute;left:0;width:1200px}

/* header */
.site-header{top:0;height:125px;background:var(--cream);border-top:2px dotted var(--orange-soft)}
.brand{position:absolute;left:110px;top:42px;display:flex;align-items:center;gap:10px}
.brand-dot{width:30px;height:30px;border-radius:50%;background:var(--orange)}
.brand-name{font-size:24px;font-weight:600;color:var(--orange)}
.main-nav{position:absolute;top:38px;left:463px;display:flex;align-items:center;height:46px}
.main-nav a{font-size:14px;color:var(--ink);text-decoration:none;text-transform:uppercase;margin-right:36px}
.main-nav a.active{background:var(--orange);color:var(--white);border-radius:16px;padding:13px 18px;margin-right:20px;box-shadow:0 2px 3px rgba(0,0,0,.2)}
.cart{position:absolute;left:1035px;top:43px;width:36px;height:36px;border-radius:50%;background:#3a3a3a}
.cart svg{position:absolute;left:10px;top:11px}
.cart-count{position:absolute;right:-6px;top:-6px;width:16px;height:16px;border-radius:50%;background:var(--orange);color:#fff;font-size:10px;text-align:center;line-height:16px}

/* hero */
.hero{top:125px;height:466px;background:linear-gradient(90deg,#d9c4b8 0%,#c7afa2 30%,var(--taupe) 60%,#ad978a 100%)}
.hero-copy{position:absolute;left:589px;top:220px;width:470px;color:var(--white)}
.hero-copy h1{font-size:60px;line-height:1;text-shadow:0 2px 3px rgba(0,0,0,.25)}
.hero-copy p{font-size:11px;line-height:25px;margin-top:26px}
.hero-arrows{position:absolute;left:590px;top:378px;display:flex;gap:9px}
.hero-arrows span{width:26px;height:26px;border-radius:50%;background:#4a4a4a;display:flex;align-items:center;justify-content:center}
.hero-arrows span:first-child{background:var(--orange)}

/* about */
.about{top:591px;height:356px;background:var(--orange)}
.about h2{position:absolute;left:111px;top:88px;font-size:42px;color:var(--white);text-shadow:0 2px 2px rgba(0,0,0,.2)}
.about p{position:absolute;left:111px;top:150px;width:575px;font-size:11px;line-height:25px;color:var(--white)}
.about-photo{position:absolute;left:722px;top:50px}

/* products */
.products{top:947px;height:424px}
.section-title{position:absolute;left:0;width:1200px;text-align:center;font-size:40px}
.products .section-title{top:60px;color:#2a2a2a;text-shadow:0 2px 2px rgba(0,0,0,.2)}
.product{position:absolute;top:152px;width:225px;height:178px}
.product svg.frame{position:absolute;inset:0}
.product h3{position:absolute;top:50px;width:100%;text-align:center;font-size:15px;font-weight:400;color:var(--ink)}
.product .shot{position:absolute;left:48px;top:96px;width:130px;height:50px;border-radius:40%;background:radial-gradient(ellipse,#c7895a 0%,#e6c7ac 60%,transparent 75%)}
.product.active h3{color:rgba(255,255,255,.45);font-size:14px;top:46px}
.price{position:absolute;top:57px;width:100%;text-align:center;font-size:28px;color:var(--white)}
.price-rule{position:absolute;left:44px;top:104px;width:137px;height:1px;background:rgba(255,255,255,.6)}
.add-cart{position:absolute;top:118px;width:100%;text-align:center;font-size:12px;color:var(--white);text-transform:uppercase}

/* blog */
.blog{top:1371px;height:428px;background:linear-gradient(180deg,#f5a556 0%,#f19d48 60%,#ee9540 100%);border-top:3px dotted #fff}
.blog .section-title{top:82px;color:var(--white);text-shadow:0 2px 2px rgba(0,0,0,.2)}
.post{position:absolute;top:173px;width:475px;height:195px;background:var(--white);box-shadow:0 3px 6px rgba(0,0,0,.25)}
.post svg{position:absolute;left:22px;top:32px}
.post h3{position:absolute;left:232px;top:36px;width:225px;font-size:14px;font-weight:400;line-height:20px;color:var(--ink)}
.post time{position:absolute;left:232px;top:84px;font-size:9px;color:var(--orange)}
.post p{position:absolute;left:232px;top:103px;width:225px;font-size:10.5px;line-height:20px;color:var(--muted)}

/* newsletter */
.newsletter{top:1799px;height:362px;background:var(--brown);border-top:3px dotted var(--orange-soft)}
.newsletter .section-title{top:52px;color:var(--white)}
.newsletter p{position:absolute;left:210px;top:127px;width:780px;text-align:center;font-size:11px;line-height:27px;color:#e8e0d8}
.signup{position:absolute;left:382px;top:221px;width:440px;height:57px}
.signup svg.bar{position:absolute;inset:0}
.signup .field{position:absolute;left:24px;top:9px;width:360px;height:39px;border-radius:20px;background:var(--field);font-size:11px;color:#8a8070;padding-left:20px;line-height:39px}
.signup .go{position:absolute;left:398px;top:16px}

/* footer */
.site-footer{top:2161px;height:129px;background:var(--cream)}
.footer-links{position:absolute;left:111px;top:43px;font-size:11px;color:var(--ink)}
.footer-links span{margin:0 6px}
.copyright{position:absolute;left:111px;top:77px;font-size:11px;color:var(--ink)}
.social{position:absolute;left:956px;top:53px;display:flex;gap:7px}
.social span{width:28px;height:28px;border-radius:50%}
</style>
</head>
<body>

<header class="site-header">
  <div class="brand"><span class="brand-dot"></span><span class="brand-name">Specs Parlour</span></div>
  <nav class="main-nav">
    <a class="active" href="#">Home</a>
    <a href="#">About Us</a>
    <a href="#">New Releases</a>
    <a href="#">Blog</a>
    <a href="#">Social</a>
    <a href="#">Contact Us</a>
  </nav>
  <div class="cart">
    <svg width="16" height="14" viewBox="0 0 16 14"><path d="M0 1h3l2 8h8l2-6H4" fill="none" stroke="#fff" stroke-width="1.6"/><circle cx="6" cy="12" r="1.3" fill="#fff"/><circle cx="12" cy="12" r="1.3" fill="#fff"/></svg>
    <span class="cart-count">0</span>
  </div>
</header>

<section class="hero" role="img" aria-label="Photo of a young child wearing large dark-framed glasses">
  <div class="hero-copy">
    <h1 class="script">Glasses Frames</h1>
    <p>Sed nibh enim, viverra ac egestas sit amet, lacinia id arcu. Donec feugiat, felis placerat bland it mollis, leo diam malesuada magna, in lobortis lorem dui quis lorem.</p>
  </div>
  <div class="hero-arrows">
    <span><svg width="8" height="8" viewBox="0 0 8 8"><path d="M5 1L2 4l3 3" fill="none" stroke="#fff" stroke-width="1.5"/></svg></span>
    <span><svg width="8" height="8" viewBox="0 0 8 8"><path d="M3 1l3 3-3 3" fill="none" stroke="#fff" stroke-width="1.5"/></svg></span>
  </div>
</section>

<section class="about">
  <h2 class="script">Specs Parlour</h2>
  <p>Vestibulum in diam arcu. Donec molestie dignissim lobortis. Donec pretium, metus sed tristique sodales, ex arcu pharetra odio, in cursus justo libero quis quam. Sed pulvinar velit in convallis bibendum. Mauris commodo lobort is dolor, quis fermentum risus rutrum a. Phasellus aliquam mi a erat luctus rhoncus. Ut sed convallis mauris. Phas ellus eleifend neque sit amet urna auctor vehicula nec ut metus. Nunc a magna ac risus volutpat ultrices quis vitae massa. Suspendisse et dui nec dui luctus iaculis eleifend a erat. Fusce nec tincidunt leo.</p>
  <svg class="about-photo" width="364" height="252" viewBox="0 0 364 252" role="img" aria-label="Photo of the storefront with parked cars">
    <defs><linearGradient id="store" x1="0" y1="0" x2="0" y2="1"><stop offset="0" stop-color="#6f9ad8"/><stop offset=".4" stop-color="#8a8f98"/><stop offset="1" stop-color="#3b3d42"/></linearGradient></defs>
    <path d="M62,32 Q62,6 94,6 H270 Q302,6 302,32 Q358,42 358,126 Q358,210 302,220 Q302,246 270,246 H94 Q62,246 62,220 Q6,210 6,126 Q6,42 62,32 Z" fill="url(#store)" stroke="#fff" stroke-width="7"/>
  </svg>
</section>

<section class="products">
  <h2 class="section-title script">Our Products</h2>

  <article class="product" style="left:111px">
    <svg class="frame" viewBox="0 0 225 178"><path d="M4,44 Q16,44 16,30 Q60,28 70,8 Q112,-2 155,8 Q165,28 209,30 Q209,44 221,44 V158 Q209,158 209,172 H16 Q16,158 4,158 Z" fill="#fff" stroke="var(--orange)" stroke-width="3"/></svg>
    <h3>Vestibulum in diam</h3>
    <div class="shot" role="img" aria-label="Product photo of brown round sunglasses"></div>
  </article>

  <article class="product" style="left:362px">
    <svg class="frame" viewBox="0 0 225 178"><path d="M4,44 Q16,44 16,30 Q60,28 70,8 Q112,-2 155,8 Q165,28 209,30 Q209,44 221,44 V158 Q209,158 209,172 H16 Q16,158 4,158 Z" fill="#fff" stroke="var(--orange)" stroke-width="3"/></svg>
    <h3>Etiam id metus sed</h3>
    <div class="shot" role="img" aria-label="Product photo of tortoiseshell cat-eye sunglasses" style="background:radial-gradient(ellipse,#2f6a6a 0%,#b7875f 55%,transparent 75%)"></div>
  </article>

  <article class="product active" style="left:612px">
    <svg class="frame" viewBox="0 0 225 178"><path d="M4,44 Q16,44 16,30 Q60,28 70,8 Q112,-2 155,8 Q165,28 209,30 Q209,44 221,44 V158 Q209,158 209,172 H16 Q16,158 4,158 Z" fill="var(--orange-soft)" stroke="var(--orange)" stroke-width="3"/></svg>
    <h3>Quisque dictum</h3>
    <div class="price">$ 45.00</div>
    <div class="price-rule"></div>
    <div class="add-cart">
      <svg width="13" height="11" viewBox="0 0 16 14" style="vertical-align:-1px;margin-right:5px"><path d="M0 1h3l2 8h8l2-6H4" fill="none" stroke="#fff" stroke-width="1.8"/><circle cx="6" cy="12" r="1.4" fill="#fff"/><circle cx="12" cy="12" r="1.4" fill="#fff"/></svg>Add to cart
    </div>
  </article>

  <article class="product" style="left:864px">
    <svg class="frame" viewBox="0 0 225 178"><path d="M4,44 Q16,44 16,30 Q60,28 70,8 Q112,-2 155,8 Q165,28 209,30 Q209,44 221,44 V158 Q209,158 209,172 H16 Q16,158 4,158 Z" fill="#fff" stroke="var(--orange)" stroke-width="3"/></svg>
    <h3>Integer at magna</h3>
    <div class="shot" role="img" aria-label="Product photo of black round eyeglasses" style="background:radial-gradient(ellipse,#e8e8e8 0%,#9a9a9a 50%,transparent 75%)"></div>
  </article>
</section>

<section class="blog" role="img" aria-label="Orange-tinted photo of a woman in glasses">
  <h2 class="section-title script">Latest Blog Posts</h2>

  <article class="post" style="left:111px">
    <svg width="188" height="130" viewBox="0 0 188 130" role="img" aria-label="Photo of black-framed glasses">
      <defs><linearGradient id="p1" x1="0" y1="0" x2="1" y2="1"><stop offset="0" stop-color="#e9dccd"/><stop offset="1" stop-color="#b9a58f"/></linearGradient></defs>
      <path d="M32,16 Q32,3 48,3 H140 Q156,3 156,16 Q185,22 185,65 Q185,108 156,114 Q156,127 140,127 H48 Q32,127 32,114 Q3,108 3,65 Q3,22 32,16 Z" fill="url(#p1)" stroke="var(--orange)" stroke-width="3"/>
    </svg>
    <h3>Nunc a magna ac risus volutpat ultrices quis vitae massa.</h3>
    <time>OCT 20, 2016</time>
    <p>Vivamus feugiat eu leo vitae tempor. Proin scelerisque odio mi, at dignissim est dapibus in. Praesent sed pretium diam.</p>
  </article>

  <article class="post" style="left:612px">
    <svg width="188" height="130" viewBox="0 0 188 130" role="img" aria-label="Photo of a woman in sunglasses sitting in a car">
      <defs><linearGradient id="p2" x1="0" y1="0" x2="1" y2="1"><stop offset="0" stop-color="#6a7a6a"/><stop offset="1" stop-color="#7a2a22"/></linearGradient></defs>
      <path d="M32,16 Q32,3 48,3 H140 Q156,3 156,16 Q185,22 185,65 Q185,108 156,114 Q156,127 140,127 H48 Q32,127 32,114 Q3,108 3,65 Q3,22 32,16 Z" fill="url(#p2)" stroke="var(--orange)" stroke-width="3"/>
    </svg>
    <h3>Proin scelerisque odio mi, at dignissim est dapibus in.</h3>
    <time>OCT 20, 2016</time>
    <p>Vivamus feugiat eu leo vitae tempor. Proin scelerisque odio mi, at dignissim est dapibus in. Praesent sed pretium diam.</p>
  </article>
</section>

<section class="newsletter">
  <h2 class="section-title script">Signup Our Newsletter</h2>
  <p>Phasellus aliquam mi a erat luctus rhoncus. Ut sed convallis mauris. Phas ellus eleifend neque sit amet urna auctor vehicula nec ut metus. Nunc a magna ac risus volutpat ultrices quis vitae massa. Suspendisse et dui nec dui luctus iaculis eleifend a erat. Fusce nec tincidunt leo.</p>
  <form class="signup">
    <svg class="bar" viewBox="0 0 440 57"><path d="M0,12 Q10,12 10,2 H430 Q430,12 440,12 V45 Q430,45 430,55 H10 Q10,45 0,45 Z" fill="var(--orange)"/></svg>
    <div class="field">Email Address</div>
    <svg class="go" width="26" height="24" viewBox="0 0 26 24"><path d="M2 12h19M13 3l9 9-9 9" fill="none" stroke="#fff" stroke-width="4" stroke-linecap="round" stroke-linejoin="round"/></svg>
  </form>
</section>

<footer class="site-footer">
  <div class="footer-links">Products<span>|</span>Privacy Policy<span>|</span>Sitemap</div>
  <div class="copyright">Copyrights@2016 Specs Parlour. All Right Reserved.</div>
  <div class="social">
    <span style="background:#3b5a96"></span>
    <span style="background:#2aa3c9"></span>
    <span style="background:#c4302b"></span>
    <span style="background:#ee7a22"></span>
  </div>
</footer>

</body>
</html>
```